New Design for Water Vending Machine

Re-design graphics for face plate of water jug vending machine.

Attached are the following:
-Picture of the current face plate for the vending machine. The layout and workflow of the system have been changed.
-Picture of the new face plate without a decal installed.
-Picture of an actual installation of these vending machines for reference.
-DXF File with layout of the face plate
-PDF File with layout notes

The graphics will be printed on a lexan decal. There will be holes cutout for the following:
-Corvel Credit card reader
-Coin reject button
-Coin slot
-4 x Buttons
-Change return
Each of the cutouts should be approximately 5mm larger in all directions than the cutout size on the DXF file.

The flow of the system is as follows:
1. Insert Coins or tap Pendra/Credit/PrePaid Card
2. Press 'Format' button until desired bottle size is displayed.
3. Press 'Start' to begin filling.
'Pause' Button may be pressed during fill to switch containers or temporarily pause fill.
A poster has also been attached that is currently displayed above the prototype machines for customer reference.

Note that the bottom button is not currently used. Perhaps the design could include a window of sorts to add a label to it down the road.

The logos for TallyCoin, Orbu and Pendra Zip could be displayed near the cutout for the Corvel system.

The phrase 'Premium Drinking Water processed by Reverse Osmosis' should be displayed somewhere on the plate.

Dimensions of the face plate are 12.75" wide x 29.75" high. Dimensions of the graphics will be 10.25" x 27".

The display window will simply be clear lexan. No material will be cutout. Buffer space around display window should be 7mm.

Requirements
Must have
• Vibrant colors, and be eye catching. We want customers to be visually appealed by the machine. It should also follow a blue color theme. Text needs to be clearly layed out, and be concise.

```html
<!DOCTYPE html>
<html lang="en">
<head>
<meta charset="utf-8">
<title>Water Vending Face Plate</title>
<link href="https://fonts.googleapis.com/css2?family=Teko:wght@300;400;500&family=Arvo:wght@700&family=Open+Sans:wght@400;700&display=swap" rel="stylesheet">
<style>
  :root {
    --plate: #dedede;
    --cut: #66b32e;
    --panel-top: #d2ddf2;
    --panel-mid: #86aee0;
    --panel-low: #5b86c8;
    --panel-deep: #34609f;
    --frame: #90abdc;
    --pill: #6fa3dc;
    --white: #ffffff;
    --accent: #ffd21f;
    --ink: #1f3f8f;
    --step-ink: #1e5aa8;
  }
  * { margin: 0; padding: 0; box-sizing: border-box; }
  html, body { width: 1200px; height: 2738px; overflow: hidden; background: #ffffff; }
  .canvas { position: relative; width: 1200px; height: 2738px; font-family: "Teko", "Oswald", sans-serif; color: var(--white); }
  .plate { position: absolute; left: 46px; top: 81px; width: 1109px; height: 2588px; background: var(--plate); border: 2px solid var(--cut); border-radius: 26px; }
  .reg { position: absolute; width: 22px; height: 22px; border: 1.5px solid #8cc86a; }
  .artwork { position: absolute; left: 144px; top: 175px; width: 911px; height: 2399px; overflow: hidden;
    background:
      radial-gradient(ellipse 70% 30% at 75% 85%, rgba(60,100,170,.55), transparent 70%),
      linear-gradient(160deg, var(--panel-top) 0%, #a9c2ea 25%, var(--panel-mid) 50%, var(--panel-low) 78%, var(--panel-deep) 100%); }
  .display-frame { position: absolute; left: 321px; top: 210px; width: 560px; height: 125px; background: var(--frame); border-radius: 26px; }
  .cutout { position: absolute; background: var(--cut); }
  .display-window { left: 344px; top: 233px; width: 511px; height: 78px; }
  .coin-reject { left: 376px; top: 497px; width: 34px; height: 34px; border-radius: 50%; }
  .coin-slot { left: 447px; top: 464px; width: 8px; height: 100px; }
  .label { position: absolute; white-space: nowrap; line-height: 1; }
  .label-small { font-size: 30px; font-weight: 300; }
  .headline { font-size: 32px; font-weight: 300; left: 244px; top: 642px; }
  .fine-print { position: absolute; left: 247px; top: 695px; font-size: 12.5px; font-weight: 300; line-height: 22px; text-transform: uppercase; }
  .reader-panel { position: absolute; left: 706px; top: 432px; width: 328px; height: 543px; background: var(--frame); border-radius: 18px; }
  .reader { left: 723px; top: 457px; width: 293px; height: 364px; }
  .card-names { position: absolute; left: 730px; top: 860px; width: 282px; display: flex; justify-content: space-between; align-items: center; }
  .card-name { font-family: "Teko", sans-serif; font-weight: 500; font-size: 30px; color: var(--ink); line-height: 1; display: flex; align-items: center; gap: 5px; white-space: nowrap; }
  .card-name .dot { width: 12px; height: 12px; border-radius: 50%; background: var(--ink); }
  .card-note { position: absolute; left: 706px; top: 928px; width: 328px; text-align: center; font-family: "Open Sans", sans-serif; font-size: 9px; color: var(--white); }
  .step { position: absolute; width: 60px; height: 60px; border-radius: 50%; background: var(--white); color: var(--step-ink); font-family: "Open Sans", sans-serif; font-weight: 700; font-size: 40px; display: flex; align-items: center; justify-content: center; box-shadow: 0 2px 4px rgba(0,0,0,.2); }
  .instruction { position: absolute; width: 460px; text-align: center; font-size: 33px; font-weight: 300; line-height: 1; }
  .instruction-pause { font-size: 26px; line-height: 31px; }
  .instruction em { font-style: normal; color: var(--accent); }
  .button-pill { position: absolute; left: 680px; width: 252px; height: 126px; border-radius: 63px; background: var(--pill); }
  .button-pill .name { position: absolute; left: 34px; top: 44px; width: 104px; text-align: center; font-size: 40px; font-weight: 300; line-height: 1; white-space: nowrap; }
  .button-pill .cutout { left: 147px; top: 20px; width: 86px; height: 86px; border-radius: 50%; }
  .change-return { left: 222px; top: 2274px; width: 278px; height: 128px; }
  .tagline { position: absolute; left: 144px; top: 2450px; width: 911px; text-align: center; font-family: "Arvo", serif; font-weight: 700; font-size: 27px; letter-spacing: 1.5px; text-shadow: 0 2px 3px rgba(0,0,0,.5); }
  .arrows { position: absolute; left: 0; top: 0; }
</style>
</head>
<body>
<div class="canvas">
  <div class="plate"></div>

  <div class="reg" style="left:94px;top:129px"></div><div class="reg" style="left:341px;top:129px"></div><div class="reg" style="left:589px;top:129px"></div><div class="reg" style="left:836px;top:129px"></div><div class="reg" style="left:1083px;top:129px"></div>
  <div class="reg" style="left:94px;top:404px"></div><div class="reg" style="left:1083px;top:404px"></div>
  <div class="reg" style="left:94px;top:678px"></div><div class="reg" style="left:1083px;top:678px"></div>
  <div class="reg" style="left:94px;top:952px"></div><div class="reg" style="left:1083px;top:952px"></div>
  <div class="reg" style="left:94px;top:1226px"></div><div class="reg" style="left:1083px;top:1226px"></div>
  <div class="reg" style="left:94px;top:1501px"></div><div class="reg" style="left:1083px;top:1501px"></div>
  <div class="reg" style="left:94px;top:1775px"></div><div class="reg" style="left:1083px;top:1775px"></div>
  <div class="reg" style="left:94px;top:2049px"></div><div class="reg" style="left:1083px;top:2049px"></div>
  <div class="reg" style="left:94px;top:2323px"></div><div class="reg" style="left:1083px;top:2323px"></div>
  <div class="reg" style="left:94px;top:2598px"></div><div class="reg" style="left:341px;top:2598px"></div><div class="reg" style="left:589px;top:2598px"></div><div class="reg" style="left:836px;top:2598px"></div><div class="reg" style="left:1083px;top:2598px"></div>

  <div class="artwork" role="img" aria-label="Background artwork: pouring stream of water with droplets and a splash in shades of blue"></div>

  <div class="display-frame"></div>
  <div class="cutout display-window"></div>

  <div class="cutout coin-reject"></div>
  <div class="cutout coin-slot"></div>

  <svg class="arrows" width="1200" height="1000" viewBox="0 0 1200 1000">
    <g stroke="#ffffff" stroke-width="3" fill="none" stroke-linecap="round">
      <path d="M253 588 H378 L420 556"/>
      <path d="M408 556 L422 553 L416 566"/>
      <path d="M531 590 H695"/>
      <path d="M684 582 L697 590 L684 598"/>
    </g>
  </svg>

  <div class="label label-small" style="left:253px;top:548px">INSERT COIN</div>
  <div class="label label-small" style="left:531px;top:550px">CREDIT CARD</div>
  <div class="label headline">INSERT CHANGE OR TAP PENDRA/CREDIT CARD</div>
  <div class="fine-print">
    Exact change no longer required! Machines will give change once start is pressed.<br>
    When tapping card, please hold your card in front of the reader for a few seconds.<br>
    If card is not held long enough, machine says 'transaction cancelled'.
  </div>

  <div class="reader-panel"></div>
  <div class="cutout reader"></div>
  <div class="card-names">
    <span class="card-name"><span class="dot"></span>TallyCoin</span>
    <span class="card-name">Orbu</span>
    <span class="card-name">Pendra Zip</span>
  </div>
  <div class="card-note">*Credit/Debit and coin combinations not accepted*</div>

  <div class="step" style="left:412px;top:809px">1</div>
  <div class="step" style="left:423px;top:1174px">2</div>
  <div class="step" style="left:417px;top:1471px">3</div>
  <div class="step" style="left:429px;top:1723px">!</div>

  <div class="instruction" style="left:228px;top:1117px">PRESS <em>FORMAT</em> BUTTON TO SELECT SIZE</div>
  <div class="instruction" style="left:228px;top:1385px">PRESS <em>START</em> BUTTON TO BEGIN FILLING</div>
  <div class="instruction instruction-pause" style="left:228px;top:1632px"><em>PAUSE</em> BUTTON MAY BE PRESSED DURING FILL<br>TO SWITCH CONTAINERS OR TEMPORARILY PAUSE FILL.</div>

  <div class="button-pill" style="top:1067px"><span class="name">FORMAT</span><span class="cutout"></span></div>
  <div class="button-pill" style="top:1328px"><span class="name">START</span><span class="cutout"></span></div>
  <div class="button-pill" style="top:1590px"><span class="name">PAUSE</span><span class="cutout"></span></div>
  <div class="button-pill" style="top:1852px"><span class="cutout"></span></div>

  <div class="cutout change-return"></div>

  <div class="tagline">Premium Drinking Water processed by Reverse Osmosis</div>
</div>
</body>
</html>
```